Updated Business Card Design more modern and eye catching

looking for something more dynamic than the sterile card we have now. Please take a look at our web site www.brindlemarket.net to see what we do. only looking for the front side of the card for now. I've also attached a sample of a card with raised spot uv ink - it might be cool to incorporate something like that. Card should be bold yet serious. No frilly or scrolly stuff on it.
Updates
Target Market(s)
We do decor and signage for retail business and supermarkets. Our new name should reflect that we're hip but serious.
Contact Information for Business Card
standard business card size - horizontal preferred
Font styles to use
Requirements
Must have
- Current logo and colors cannot be changed.
Nice to have
- Must have information shown on existing card but open to some changes. Okay to consider spot uv.
Should not have
- Not busy with pictures in the background.

```html
<!DOCTYPE html>
<html lang="en">
<head>
<meta charset="utf-8">
<title>Brindle Market – Business Card</title>
<link href="https://fonts.googleapis.com/css2?family=Maven+Pro:wght@400;500;600&display=swap" rel="stylesheet">
<style>
  :root {
    --page: #f4f4f4;
    --card-dark: #141414;
    --card-light: #ffffff;
    --gold: #b3a654;
    --ink: #1c1c1c;
    --ink-soft: #2e2e2e;
    --ring: #3a3a3a;
    --white: #ffffff;
  }
  * { margin: 0; padding: 0; box-sizing: border-box; }
  html, body { width: 1200px; height: 900px; overflow: hidden; }
  body {
    background: var(--page);
    font-family: "Maven Pro", "Helvetica Neue", Arial, sans-serif;
    position: relative;
  }
  .card { position: absolute; }

  /* Card face: dark */
  .card--front {
    left: 291px; top: 78px; width: 619px; height: 354px;
    background: var(--card-dark);
    overflow: hidden;
  }
  .front__ring { position: absolute; left: 287px; top: 22px; }
  .front__brand {
    position: absolute; left: 32px; top: 278px;
    display: flex; align-items: center; gap: 10px;
  }
  .brand-square {
    width: 22px; height: 22px; border: 2px solid var(--gold);
  }
  .front__name {
    font-size: 23px; font-weight: 500; letter-spacing: 1px;
    color: var(--gold); text-transform: uppercase;
  }
  .front__web {
    position: absolute; left: 32px; top: 307px;
    font-size: 16px; color: var(--white); letter-spacing: 0.2px;
  }

  /* Card face: light */
  .card--back {
    left: 288px; top: 465px; width: 625px; height: 357px;
    background: var(--card-light);
    overflow: hidden;
  }
  .back__band {
    position: absolute; left: 0; bottom: 0; width: 100%; height: 12px;
    background: var(--gold);
  }
  .back__brand {
    position: absolute; left: 92px; top: 86px;
    display: flex; align-items: center; gap: 18px;
  }
  .back__brand .brand-square { width: 40px; height: 40px; border-width: 3px; border-color: var(--ink); }
  .back__name {
    font-size: 42px; font-weight: 500; letter-spacing: 1.5px;
    color: var(--ink); text-transform: uppercase;
  }
  .person {
    position: absolute; right: 333px; top: 188px; text-align: right;
  }
  .person__name { font-size: 20px; color: var(--ink-soft); letter-spacing: 0.5px; }
  .person__first { color: var(--gold); font-weight: 600; }
  .person__title { font-size: 15px; color: var(--ink-soft); margin-top: 2px; }
  .person__address { font-size: 16px; color: var(--gold); line-height: 25px; margin-top: 6px; }

  .contacts {
    position: absolute; left: 326px; top: 188px; list-style: none;
  }
  .contacts li {
    display: flex; align-items: center; gap: 10px;
    height: 25px; font-size: 16px; color: var(--ink-soft);
  }
  .contacts svg { width: 18px; height: 18px; fill: var(--gold); flex: none; }
  .contacts .ext { color: var(--gold); margin-left: 4px; }
</style>
</head>
<body>

<section class="card card--front">
  <svg class="front__ring" width="310" height="310" viewBox="0 0 310 310" aria-hidden="true">
    <circle cx="155" cy="155" r="151" fill="none" stroke="var(--ring)" stroke-width="5"/>
  </svg>
  <div class="front__brand">
    <span class="brand-square"></span>
    <span class="front__name">Brindle Market</span>
  </div>
  <p class="front__web">www.brindlemarket.net</p>
</section>

<section class="card card--back">
  <div class="back__brand">
    <span class="brand-square"></span>
    <span class="back__name">Brindle Market</span>
  </div>

  <div class="person">
    <p class="person__name"><span class="person__first">MARLA</span> KEATON</p>
    <p class="person__title">Vice-President</p>
    <p class="person__address">4120 Harbor Point<br>Way Fort Pierce, Fl 34946</p>
  </div>

  <ul class="contacts">
    <li>
      <svg viewBox="0 0 24 24" aria-hidden="true"><path d="M3 8c0-2 4-4 9-4s9 2 9 4v2h-5V8H8v2H3z M6 11h12l2 9H4z"/></svg>
      <span>561 830 4417<span class="ext">ext. 3</span></span>
    </li>
    <li>
      <svg viewBox="0 0 24 24" aria-hidden="true"><path d="M7 2h10a1 1 0 0 1 1 1v18a1 1 0 0 1-1 1H7a1 1 0 0 1-1-1V3a1 1 0 0 1 1-1zm1 3v12h8V5zm4 13.5a1 1 0 1 0 0 2 1 1 0 0 0 0-2z"/></svg>
      <span>404 615 2289</span>
    </li>
    <li>
      <svg viewBox="0 0 24 24" aria-hidden="true"><path d="M2 6h20v12H2z" /><path d="M2 6l10 7 10-7" fill="none" stroke="#fff" stroke-width="1.6"/></svg>
      <span>marlak@brindlemarket.net</span>
    </li>
    <li>
      <svg viewBox="0 0 24 24" aria-hidden="true"><circle cx="12" cy="12" r="9"/><path d="M12 3v18M3 12h18M12 3c-4 4-4 14 0 18M12 3c4 4 4 14 0 18" fill="none" stroke="#fff" stroke-width="1.2"/></svg>
      <span>www.brindlemarket.net</span>
    </li>
  </ul>

  <div class="back__band"></div>
</section>

</body>
</html>
```